Labels/logo for luxury bath products

I am developing a range of luxury bath foams - aimed at the top end of the luxury market. My company name is VEM (very basic website can be seen at www.vemarton.example).

I am looking for a label design for the front of the bottle, which should incorporate the VEM logo as per the website (file attached), but embedded within a more intricate label design. I provide a link to a picture of the bottle below.

The bath foam will come in four fragrances: Vetiver, Sandalwood, Jasmine and Neroli. The label should include the fragrance name. So the label must include the brand name 'VEM' and the name of the fragrance - e.g. Sandalwood Bath Foam, Neroli Bath Foam, etc.

The products are aimed at both the male and female market and so shouldn't be too feminine.

A brand to take inspiration from is Lune Bravière: http://www.lunebraviere.example/ - I like the labels that they use on their products, which is a gold embossed crest, which they use as the label for their products. I am not referring to their font, but to their label design - I like the embossed label, and am quite keen on metallics.

Conversely, I would like to add a contemporary edge to this design - I like the striping and contemporary fonts on this design: http://www.hadley-frost.example/images/fac83.jpg

My brand also harnesses the powers of natural flower ingredients, and so I am inspired by the products of Quenby - quenby.example. This labelling is more clinical and scientific.

Ideally I would like a label which combines these elements - i.e. a luxury label with a contemporary feel, that incorporate the scientific nature of the product.

The design needs to communicate high end luxury. The bottle is however apothecary style, and a nod to science and botany would be good. I would however like a bold approach to this design - it is a modern brand.

The bottle being used for the product can be seen at: http://www.tavel-vitro.example/en/product-groups/8-Apothecary-bottles - these are extremely expensive bottles and the label needs to reflect this quality. These bottles are traditional in design, but incorporate high end glassware technology to preserve the integrity of the natural ingredients. Therefore the product is a mix of old and new, and the label could also reflect this. The colour of the glass is very deep purple.

The front label does not need information such as weight/volume - it purely needs a label which will recognise it as the VEM brand, with the product name. I am looking for a high quality label, which is unique. I am happy to print embossed labels and to use foils on my labels.

Please do not be boring! I appreciate I have given a variety of influences, so summarise the requirements are a mix of:

a bold design
contemporary
luxury

The label must include NO slogans.

I am looking to build a relationship with a graphic designer for packaging and website design requirements so this will be the first of many projects.

Target Market(s)

Luxury end of market - clientele will like luxury and will pay for the highest quality ingredients in the product, but will also appreciate the botanical nature of the product.

Industry/Entity Type

Graphic Designer

Requirements
Must have
• Must include the company name, VEM, although this doesn't need to be particularly prominent. And the product name, e.g. Sandalwood.
Nice to have
• It should combine luxury, but with recognition of the science behind the product.
Should not have
• No slogans, minimal wording on the front label. No other wording other than company name and product name. No primary colours.

```html
<!DOCTYPE html>
<html lang="en">
<head>
<meta charset="utf-8">
<title>VEM Neroli Bath Foam – Front Label</title>
<link rel="stylesheet" href="https://fonts.googleapis.com/css2?family=Cinzel:wght@500;900&display=swap">
<style>
  :root {
    --page-bg: #f1f1f3;
    --gold-light: #f4e3b0;
    --gold-mid: #d9b86a;
    --gold-deep: #a87d2e;
    --panel-light: #f3e2ae;
    --panel-deep: #d5b872;
    --band-navy: #0b1433;
    --band-blue: #1a2a68;
    --edge-dark: #05070f;
    --ink: #0a0d1f;
    --flourish: #b08435;
  }
  html, body {
    margin: 0;
    padding: 0;
    width: 751px;
    height: 1200px;
    overflow: hidden;
    background: var(--page-bg);
  }
  .canvas {
    position: relative;
    width: 751px;
    height: 1200px;
  }
  .label {
    position: absolute;
    left: 95.5px;
    top: 212px;
    width: 560px;
    height: 775px;
  }
  .brand-name {
    font-family: "Cinzel", serif;
    font-weight: 900;
    fill: var(--ink);
    letter-spacing: 1px;
  }
  .fragrance-name {
    font-family: "Cinzel", serif;
    font-weight: 500;
    fill: var(--ink);
    letter-spacing: 1px;
  }
  .product-type {
    font-family: "Cinzel", serif;
    font-weight: 500;
    fill: var(--ink);
    letter-spacing: 0.5px;
  }
</style>
</head>
<body>
<main class="canvas">
  <svg class="label" viewBox="0 0 300 415" xmlns="http://www.w3.org/2000/svg" aria-label="VEM Neroli Bath Foam label">
    <defs>
      <path id="crest-shape" d="M60,58 Q150,-25 240,58 L258,58 L258,88 Q300,100 300,208 Q300,316 258,330 L258,358 L240,358 Q150,440 60,358 L42,358 L42,330 Q0,316 0,208 Q0,100 42,88 L42,58 Z"/>
      <linearGradient id="gold-frame" x1="0" y1="0" x2="1" y2="1">
        <stop offset="0" stop-color="var(--gold-light)"/>
        <stop offset="0.45" stop-color="var(--gold-mid)"/>
        <stop offset="0.7" stop-color="var(--gold-deep)"/>
        <stop offset="1" stop-color="var(--gold-light)"/>
      </linearGradient>
      <radialGradient id="gold-panel" cx="0.5" cy="0.45" r="0.65">
        <stop offset="0" stop-color="var(--panel-light)"/>
        <stop offset="1" stop-color="var(--panel-deep)"/>
      </radialGradient>
      <linearGradient id="band-fill" x1="0" y1="0" x2="1" y2="1">
        <stop offset="0" stop-color="var(--band-blue)"/>
        <stop offset="0.5" stop-color="var(--band-navy)"/>
        <stop offset="1" stop-color="var(--band-blue)"/>
      </linearGradient>
      <radialGradient id="flourish-glow" cx="0.5" cy="0.5" r="0.5">
        <stop offset="0" stop-color="var(--flourish)" stop-opacity="0.45"/>
        <stop offset="0.6" stop-color="var(--flourish)" stop-opacity="0.22"/>
        <stop offset="1" stop-color="var(--flourish)" stop-opacity="0"/>
      </radialGradient>
    </defs>

    <g class="frame-outer">
      <use href="#crest-shape" fill="url(#gold-frame)"/>
    </g>
    <g class="frame-edge" transform="translate(150 208) scale(0.965) translate(-150 -208)">
      <use href="#crest-shape" fill="var(--edge-dark)"/>
    </g>
    <g class="striped-band" role="img" aria-label="Navy band with diagonal blue stripes" transform="translate(150 208) scale(0.95) translate(-150 -208)">
      <use href="#crest-shape" fill="url(#band-fill)"/>
    </g>
    <g class="panel-rim" transform="translate(150 208) scale(0.86 0.93) translate(-150 -208)">
      <use href="#crest-shape" fill="url(#gold-frame)"/>
    </g>
    <g class="panel-edge" transform="translate(150 208) scale(0.835 0.91) translate(-150 -208)">
      <use href="#crest-shape" fill="var(--gold-deep)" opacity="0.6"/>
    </g>
    <g class="inner-panel" transform="translate(150 208) scale(0.825 0.9) translate(-150 -208)">
      <use href="#crest-shape" fill="url(#gold-panel)"/>
    </g>

    <rect class="flourish-top" role="img" aria-label="Gold baroque scroll ornament framing the brand name" x="45" y="55" width="210" height="130" fill="url(#flourish-glow)"/>
    <rect class="flourish-bottom" role="img" aria-label="Gold baroque scroll ornament below the brand name" x="60" y="228" width="180" height="38" fill="url(#flourish-glow)"/>

    <text class="brand-name" x="150" y="216" text-anchor="middle" font-size="50">VEM</text>
    <text class="fragrance-name" x="150" y="305" text-anchor="middle" font-size="17">NEROLI</text>
    <text class="product-type" x="150" y="324" text-anchor="middle" font-size="11.5">BATH FOAM</text>
  </svg>
</main>
</body>
</html>
```